Business Card for Ferncliff Massage

I need a business card for my massage therapy & cannabis oil practice. I already have a logo,the "massage" got edited out of this file. I will send the original soon. I need these elements to be on the card:
web: FerncliffMassage.example
ph: 417/283-9061
email: Mirela.Dawkant@mailbox.example
Other slogans, statements to consider:
Science Geek, Massage Therapist, Neuromuscular Therapy, Cannabis Spa Treatments, Raindrop Therapy, Essential Oils
Target Market(s)
women between 20 & 65, people with enough $ to afford regular massage, people who recently had a motor vehicle accident, Halvora HMP insured
Industry/Entity Type
Massage Therapy
Contact Information for Business Card
I would like to see my bear logo featured; contact details, greens & blues preferred colors.

```html
<!DOCTYPE html>
<html lang="en">
<head>
<meta charset="utf-8">
<title>Ferncliff Massage – Business Card</title>
<link rel="stylesheet" href="https://fonts.googleapis.com/css2?family=Ubuntu+Condensed&family=Ubuntu:wght@400;500;700&display=swap">
<style>
  :root {
    --backdrop: #dcd6c8;
    --card: #ede0c2;
    --green: #2f8a45;
    --green-soft: #4fa060;
    --stone: #a89a8c;
    --stone-dark: #7f756d;
    --text-grey: #8c837a;
  }
  * { box-sizing: border-box; margin: 0; padding: 0; }
  html, body {
    width: 1200px;
    height: 1000px;
    overflow: hidden;
    background: var(--backdrop);
  }
  .canvas {
    position: relative;
    width: 1200px;
    height: 1000px;
  }
  .card {
    position: absolute;
    left: 350px;
    top: 70px;
    width: 500px;
    height: 860px;
    background: var(--card);
    overflow: hidden;
    box-shadow: 0 6px 24px rgba(60, 50, 40, 0.18);
  }
  .vertical {
    position: absolute;
    writing-mode: vertical-rl;
    transform: rotate(180deg);
    white-space: nowrap;
  }
  .contact {
    left: 40px;
    top: 40px;
    height: 480px;
    display: flex;
    flex-direction: column;
    gap: 22px;
    font-family: "Ubuntu Condensed", sans-serif;
    font-size: 21px;
    color: var(--green);
  }
  .contact-line {
    display: flex;
    align-items: center;
    justify-content: flex-start;
    gap: 14px;
  }
  .contact-line svg {
    transform: rotate(180deg);
    flex: none;
  }
  .contact-line span { display: block; text-align: right; }
  .contact-list { height: 100%; display: flex; flex-direction: column; gap: 22px; }
  .contact-line { flex-direction: row-reverse; justify-content: flex-end; }
  .name {
    left: 72px;
    bottom: 40px;
    font-family: "Ubuntu Condensed", sans-serif;
    font-size: 30px;
    color: var(--text-grey);
  }
  .name strong { color: var(--green); font-weight: 400; font-family: "Ubuntu", sans-serif; font-weight: 700; font-size: 27px; }
  .wordmark {
    left: 200px;
    top: 250px;
    height: 400px;
    display: flex;
    flex-direction: row;
    align-items: flex-end;
    gap: 6px;
  }
  .wordmark-name {
    font-family: "Ubuntu Condensed", sans-serif;
    font-size: 84px;
    line-height: 1;
    color: var(--green);
  }
  .wordmark-tag {
    font-family: "Ubuntu", sans-serif;
    font-size: 17px;
    letter-spacing: 0.42em;
    color: var(--text-grey);
    line-height: 1;
  }
  .logo-art {
    position: absolute;
    right: 0;
    top: 30px;
    width: 200px;
    height: 800px;
    background: linear-gradient(180deg,
      var(--stone-dark) 0%, var(--stone-dark) 12%,
      var(--green-soft) 18%, var(--green) 30%,
      var(--stone-dark) 38%, var(--stone-dark) 52%,
      var(--stone) 60%, var(--stone) 100%);
    border-radius: 90px 0 0 120px;
    opacity: 0.9;
  }
</style>
</head>
<body>
<main class="canvas">
  <article class="card">
    <div class="vertical contact" style="left:auto; right:auto; left:40px;">
      <div class="contact-line">
        <span>FerncliffMassage.example</span>
        <svg width="18" height="18" viewBox="0 0 18 18" aria-hidden="true"><circle cx="9" cy="9" r="8" fill="var(--stone)"/><circle cx="9" cy="9" r="4" fill="none" stroke="var(--card)" stroke-width="1.6"/></svg>
      </div>
      <div class="contact-line">
        <span>417/283-9061</span>
        <svg width="18" height="18" viewBox="0 0 18 18" aria-hidden="true"><circle cx="9" cy="9" r="8" fill="var(--stone)"/><path d="M6 5 l2 0 l1 3 l-1.5 1 a6 6 0 0 0 2.5 2.5 l1-1.5 l3 1 l0 2 a1 1 0 0 1-1 1 a9 9 0 0 1-8-8 a1 1 0 0 1 1-1z" fill="var(--card)"/></svg>
      </div>
      <div class="contact-line">
        <span>Mirela.Dawkant@mailbox.example</span>
        <svg width="18" height="18" viewBox="0 0 18 18" aria-hidden="true"><circle cx="9" cy="9" r="8" fill="var(--stone)"/><text x="9" y="12.5" text-anchor="middle" font-size="10" font-family="Ubuntu, sans-serif" fill="var(--card)">@</text></svg>
      </div>
    </div>

    <div class="vertical name"><strong>Mirela</strong>Dawkant</div>

    <div class="vertical wordmark">
      <span class="wordmark-name">Ferncliff</span>
      <span class="wordmark-tag">MASSAGE EDUCATION</span>
    </div>

    <div class="logo-art" role="img" aria-label="Logo illustration area: stacked stones above a bear figure"></div>
  </article>
</main>
</body>
</html>
```